New SEO and Digital Marketing Company Needs Web Design

We need a web design for a new digital marketing and search engine optimisation consultancy company located in Australia called 'Bold Walrus'.

Bold Walrus helps other businesses improve their online presence through social media, search engine optimisation, and teaching businesses how to interact with clients online in a professional manner.

The web design needs to be simple but sophisticated and easy for visitors to navigate. Inspiration can be taken from the logo which is included with the brief.

Sections we would like the website to include are blog posts, FAQs, contact us, about us, and information on our services as well as a form section where potential clients can submit their details and a URL to their website for a quote or to organise a consultation. We also need the design to seamlessly incorporate social media.

A very basic example of layout has been uploaded. Feel free to use it for inspiration, but we're happy for you to come up with someone yourself.

Our current place-holder website is Joomla based.

Target Market(s)

Other businesses

Industry/Entity Type

Business Consultant

Coding

Coded - Design and coding required

Number of Pages Required

5+ page

Requirements
Must have
• Complements our logo
• Clean and sophisticated
• Blog
• Expandable and collapsible FAQs section
• Contact form where people can submit website URL as well as contact details and a message
• Able to integrate with social media
• Joomla based

```html
<!DOCTYPE html>
<html lang="en">
<head>
<meta charset="utf-8">
<title>Home – Bold Walrus</title>
<link rel="stylesheet" href="https://fonts.googleapis.com/css2?family=Roboto:wght@300;400;500;700&display=swap">
<style>
:root{
  --purple:#8e1a85;
  --purple-dark:#7a1572;
  --green:#8cc21b;
  --text:#333;
  --muted:#8a8a8a;
  --line:#dcdcdc;
  --footer-bg:#f1f1f1;
  --bottom-bg:#3b3b3b;
}
*{box-sizing:border-box;margin:0;padding:0}
html,body{width:842px;height:1200px;overflow:hidden;background:#fff}
body{position:relative;font-family:'Roboto',Arial,sans-serif;color:var(--text)}
.abs{position:absolute}

/* header */
.page-title{left:69px;top:38px;font-size:27px;font-weight:300;color:#666}
.brand{left:600px;top:42px;width:172px;display:flex;align-items:center;justify-content:flex-end;gap:8px}
.brand-square{width:10px;height:10px;background:var(--purple)}
.brand-name{font-size:18px;font-weight:500;color:var(--purple)}

/* nav */
.main-nav{left:0;top:108px;width:842px;height:30px;background:var(--purple)}
.main-nav a{position:absolute;top:0;height:30px;line-height:30px;font-size:8.5px;color:#fff;text-decoration:none;text-transform:uppercase;letter-spacing:.2px}
.main-nav a.active{background:var(--purple-dark);padding:0 20px}

/* hero */
.hero{left:0;top:138px;width:842px;height:322px;background:linear-gradient(135deg,#9a6a3e 0%,#b98552 40%,#a4703f 70%,#8a5b33 100%)}
.hero-card{left:70px;top:254px;width:221px;height:112px;background:rgba(255,255,255,.9);padding:12px 12px}
.hero-card h2{font-size:18px;font-weight:500;color:var(--purple);margin-bottom:8px}
.hero-card p{font-size:7.4px;line-height:12px;color:#444}
.btn-green{display:inline-block;background:var(--green);color:#fff;font-size:7.5px;padding:5px 7px;text-decoration:none}
.hero-card .btn-green{margin-top:9px}
.arrow{top:287px;width:20px;height:28px;background:rgba(40,40,40,.7)}
.arrow svg{display:block;margin:6px auto}

/* services */
.service{top:494px;width:206px}
.service svg{display:block;height:24px}
.service h3{font-size:16.5px;font-weight:500;color:var(--purple);margin:12px 0 9px}
.service p{font-size:7.2px;line-height:13.2px;color:var(--muted);margin-bottom:12px}

.rule{left:70px;top:716px;width:702px;height:1px;background:var(--line)}

/* blog */
.section-title{font-size:16.5px;font-weight:400;color:var(--purple)}
.blog-img{left:100px;top:780px;width:97px;height:150px;background:linear-gradient(160deg,#cfd6dc,#9a8a80 60%,#6c5e56)}
.blog-body{left:209px;top:780px;width:185px}
.blog-body h4{font-size:8px;font-weight:400;line-height:12px;color:#222;margin-bottom:6px}
.blog-body p{font-size:6.6px;line-height:12px;color:var(--muted);margin-bottom:8px}
.btn-grey{display:inline-block;background:#e2e2e2;color:#666;font-size:7.2px;padding:5px 7px;text-decoration:none}
.vdivider{left:420px;top:746px;width:1px;height:190px;background:var(--line)}

/* quote form */
.field{height:26px;border:1px solid #cfcfcf;font-size:7.5px;color:#777;padding:0 10px;line-height:24px;background:#fff}
.submit{left:459px;top:906px;width:51px;height:24px;background:#9a9a9a;color:#fff;font-size:8px;line-height:24px;text-align:center}

/* footer */
.footer{left:0;top:978px;width:842px;height:155px;background:var(--footer-bg)}
.footer h5{font-size:9px;font-weight:400;color:#222;margin-bottom:10px}
.footer p,.footer li{font-size:7px;line-height:12px;color:var(--muted)}
.contact-line{display:flex;align-items:center;gap:6px;margin-bottom:7px}
.recent{list-style:none}
.recent li{margin-bottom:3px;padding-left:7px;position:relative}
.recent li::before{content:"•";position:absolute;left:0}
.fdiv{top:996px;width:1px;height:118px;background:var(--line)}
.footer .btn-grey{position:absolute;top:116px}

/* bottom bar */
.bottom{left:0;top:1133px;width:842px;height:67px;background:var(--bottom-bg);color:#e0e0e0}
.bottom-links{left:70px;top:21px;font-size:7px}
.bottom-links span{margin:0 4px;color:#aaa}
.copyright{left:70px;top:40px;font-size:7px}
.social{top:25px;width:19px;height:19px;border-radius:50%}
</style>
</head>
<body>

<header>
  <h1 class="abs page-title">Home</h1>
  <div class="abs brand">
    <span class="brand-square"></span>
    <span class="brand-name">Bold Walrus</span>
  </div>
</header>

<nav class="abs main-nav">
  <a class="active" style="left:68px">Home</a>
  <a style="left:153px">About Us</a>
  <a style="left:235px">SEO Services</a>
  <a style="left:334px">Business Services</a>
  <a style="left:458px">Website Services</a>
  <a style="left:577px">FAQs</a>
  <a style="left:638px">Blog</a>
  <a style="left:700px">Contact Us</a>
</nav>

<section class="abs hero" role="img" aria-label="Overhead photo of a team working around a wooden desk with laptops, keyboards, charts and coffee cups"></section>
<div class="abs hero-card">
  <h2>Aliquam erat volutpat</h2>
  <p>Nunc sit amet consequat risus. Curabitur ac elit leo. In eleifend dui tellus, in scelerisque elit porttitor et. Integer eu massa lacinia, lacinia nulla non.</p>
  <a class="btn-green">Read more</a>
</div>
<div class="abs arrow" style="left:0"><svg width="8" height="16" viewBox="0 0 8 16"><path d="M7 1 1 8l6 7" fill="none" stroke="#fff" stroke-width="1.2"/></svg></div>
<div class="abs arrow" style="left:822px"><svg width="8" height="16" viewBox="0 0 8 16"><path d="M1 1l6 7-6 7" fill="none" stroke="#fff" stroke-width="1.2"/></svg></div>

<section class="abs service" style="left:72px">
  <svg viewBox="0 0 26 24" width="26"><path d="M25 1 1 11l8 3 2 9 4-6 6 4z" fill="var(--purple)"/><path d="M9 14 25 1 12 16" fill="none" stroke="#fff" stroke-width="1"/></svg>
  <h3>SEO Services</h3>
  <p>Aenean sed quam non sapien faucibus consequat vitae sit amet orci. Praesent quis risus mi. In mollis nulla in pulvinar dictum. Vivamus interdum sagittis felis, ut dapibus ligula feugiat ac. In dictum sapien eu tellus finibus fermentum. Aenean faucibus lacus ut mollis commodo. Donec vestibulum odio sem, ac laoreet massa ullamcorper id. Donec molestie nisi et tellus hendrerit vehicula.</p>
  <a class="btn-green">Read more</a>
</section>
<section class="abs service" style="left:316px">
  <svg viewBox="0 0 26 24" width="26"><rect x="9" y="2" width="8" height="5" fill="none" stroke="var(--purple)" stroke-width="2"/><rect x="1" y="6" width="24" height="17" rx="2" fill="var(--purple)"/><rect x="1" y="13" width="24" height="1.5" fill="#fff"/><rect x="11" y="11" width="4" height="5" fill="#fff"/></svg>
  <h3>Business Services</h3>
  <p>Aenean sed quam non sapien faucibus consequat vitae sit amet orci. Praesent quis risus mi. In mollis nulla in pulvinar dictum. Vivamus interdum sagittis felis, ut dapibus ligula feugiat ac. In dictum sapien eu tellus finibus fermentum. Aenean faucibus lacus ut mollis commodo. Donec vestibulum odio sem, ac laoreet massa ullamcorper id. Donec molestie nisi et tellus hendrerit vehicula.</p>
  <a class="btn-green">Read more</a>
</section>
<section class="abs service" style="left:559px">
  <svg viewBox="0 0 26 24" width="26"><rect x="1" y="1" width="24" height="16" rx="1" fill="none" stroke="var(--purple)" stroke-width="2.5"/><rect x="11" y="17" width="4" height="4" fill="var(--purple)"/><rect x="6" y="21" width="14" height="2.5" fill="var(--purple)"/></svg>
  <h3>Website Services</h3>
  <p>Aenean sed quam non sapien faucibus consequat vitae sit amet orci. Praesent quis risus mi. In mollis nulla in pulvinar dictum. Vivamus interdum sagittis felis, ut dapibus ligula feugiat ac. In dictum sapien eu tellus finibus fermentum. Aenean faucibus lacus ut mollis commodo. Donec vestibulum odio sem, ac laoreet massa ullamcorper id. Donec molestie nisi et tellus hendrerit vehicula.</p>
  <a class="btn-green">Read more</a>
</section>

<div class="abs rule"></div>

<h2 class="abs section-title" style="left:99px;top:746px">Blog</h2>
<div class="abs blog-img" role="img" aria-label="Photo of a hand holding a smartphone showing a social feed"></div>
<article class="abs blog-body">
  <h4>Neque porro quisquam est, qui dolorem ipsum quia dolor sit amet.</h4>
  <p>Sed quia non numquam eius modi tempora incidunt ut labore et dolore magnam aliquam quaerat voluptatem. Ut enim ad minima veniam, quis nostrum exercitationem ullam corporis suscipit laboriosam, nisi ut aliquid ex ea commodi consequatur? Quis autem vel eum iure reprehenderit qui in ea voluptate velit esse quam nihil molestiae consequatur. Quisque aliquet ex nec est vestibulum pulvinar.</p>
  <a class="btn-grey">Read more</a>
</article>
<div class="abs vdivider"></div>

<h2 class="abs section-title" style="left:458px;top:746px">Request a Quote</h2>
<div class="abs field" style="left:459px;top:783px;width:131px">Name</div>
<div class="abs field" style="left:603px;top:783px;width:131px">Email</div>
<div class="abs field" style="left:459px;top:825px;width:131px">Phone</div>
<div class="abs field" style="left:603px;top:825px;width:131px">Company</div>
<div class="abs field" style="left:459px;top:867px;width:275px">Address</div>
<div class="abs submit">SUBMIT</div>

<footer class="abs footer">
  <div class="abs" style="left:72px;top:18px;width:120px;height:137px">
    <h5>Contact us</h5>
    <p style="margin-bottom:7px">Bold Walrus</p>
    <div class="contact-line"><svg width="7" height="8" viewBox="0 0 7 8"><path d="M1 0h4l2 2v6H1z" fill="#999"/></svg><p>PO Box 218, Linwood VIC 3391</p></div>
    <div class="contact-line"><svg width="7" height="8" viewBox="0 0 7 8"><path d="M1 0c1 0 2 2 1 3 0 1 1 3 3 3 1-1 2 0 2 1s-1 1-2 1C2 8 0 4 0 1c0-1 1-1 1-1z" fill="#999"/></svg><p>0400 123 456</p></div>
    <div class="contact-line"><svg width="7" height="6" viewBox="0 0 7 6"><rect width="7" height="6" fill="#999"/><path d="M0 0l3.5 3L7 0" fill="none" stroke="#f1f1f1" stroke-width=".8"/></svg><p>info@boldwalrus.com.au</p></div>
    <a class="btn-grey" style="left:0">Read more</a>
  </div>
  <div class="abs" style="left:233px;top:18px;width:280px;height:137px">
    <h5>About Us</h5>
    <p>Phasellus nisl est, condimentum vitae faucibus in, sollicitudin vel metus. Nunc sit amet consequat risus. Curabitur ac elit leo. In eleifend dui tellus, in scelerisque elit porttitor et. Integer eu massa lacinia, lacinia nulla non, volutpat purus. Sed libero felis, vestibulum et dolor eget, lacinia aliquet neque. Proin porta fermentum ipsum, vel porttitor turpis venenatis luctus. Vivamus volutpat eu sapien quis tempus. Aenean feugiat viverra lorem ac sagittis.</p>
    <a class="btn-grey" style="left:0">Read more</a>
  </div>
  <div class="abs" style="left:558px;top:18px;width:215px;height:137px">
    <h5>Recent Blog Posts</h5>
    <ul class="recent">
      <li>Integer eu massa lacinia, lacinia nulla non, volutpat purus</li>
      <li>Aenean sed quam non sapien faucibus</li>
      <li>Proin porta fermentum ipsum, vel porttitor turpis</li>
      <li>Nullam accumsan purus vel tempus viverra. Mauris suscipit felis id nunc elementum varius.</li>
    </ul>
    <a class="btn-grey" style="left:0">Read more</a>
  </div>
</footer>
<div class="abs fdiv" style="left:206px"></div>
<div class="abs fdiv" style="left:534px"></div>

<div class="abs bottom">
  <div class="abs bottom-links">Home<span>|</span>About Us<span>|</span>SEO Services<span>|</span>Business Services<span>|</span>Website Services<span>|</span>FAQs<span>|</span>Blog<span>|</span>Contact Us</div>
  <div class="abs copyright">Copyright © 2015 &nbsp;Bold Walrus. &nbsp;All rights reserved.</div>
  <div class="abs social" style="left:727px;background:#3b5998"></div>
  <div class="abs social" style="left:752px;background:#2aa9e0"></div>
</div>

</body>
</html>
```